Stop Light images

I need a better traffic light graphic designed for insertion onto a report. I will upload a copy of the report so you can see what I mean. The design should be single fronted (not the traffic light hoods on the two sides) but really needs to be modern ans pop.

I need 3 designs, one with the red light glowing, one with the orange light glowing and one with the green light glowing. When the lights are glowing you must still be able to see the other colours but not illuminated.

```html
<!DOCTYPE html>
<html lang="en">
<head>
<meta charset="utf-8">
<title>Market Signal Report – July 2014</title>
<link href="https://fonts.googleapis.com/css2?family=Carlito:wght@400;700&display=swap" rel="stylesheet">
<style>
  :root {
    --ink: #111111;
    --paper: #ffffff;
    --brand-grey: #6f6f6f;
    --brand-green: #4aa142;
    --band-red: #d4401f;
    --band-orange: #e8a323;
    --band-green: #4ea64a;
    --frame-red: #e0201f;
    --rule: #444444;
    --arrow: #8a8a8a;
    --lamp-red-off: #5a1c1a;
    --lamp-orange-off: #5e3c12;
    --lamp-green-off: #17451c;
    --lamp-red-on: #ff2d24;
    --lamp-orange-on: #ffae1a;
    --lamp-green-on: #2ff04a;
  }
  * { box-sizing: border-box; margin: 0; padding: 0; }
  html, body { width: 850px; height: 1200px; overflow: hidden; background: var(--paper); }
  body { font-family: "Carlito", "Calibri", sans-serif; color: var(--ink); position: relative; }

  .signal { overflow: visible; }
  .signal-green  { --r: var(--lamp-red-off); --o: var(--lamp-orange-off); --g: var(--lamp-green-on);  --rh: 0; --oh: 0; --gh: 1; }
  .signal-orange { --r: var(--lamp-red-off); --o: var(--lamp-orange-on);  --g: var(--lamp-green-off); --rh: 0; --oh: 1; --gh: 0; }
  .signal-red    { --r: var(--lamp-red-on);  --o: var(--lamp-orange-off); --g: var(--lamp-green-off); --rh: 1; --oh: 0; --gh: 0; }

  .brand { position: absolute; left: 80px; top: 80px; display: flex; align-items: center; gap: 10px; }
  .brand-mark { width: 30px; height: 30px; background: var(--brand-green); }
  .brand-name { font-size: 44px; font-weight: 700; color: var(--brand-grey); letter-spacing: -0.5px; line-height: 1; }

  .report-meta { position: absolute; left: 420px; top: 70px; width: 346px; border: 2px solid var(--ink); border-collapse: collapse; font-size: 12px; font-weight: 700; }
  .report-meta td { padding: 1px 4px; border-bottom: 1px solid var(--ink); height: 16px; white-space: nowrap; }
  .report-meta tr:last-child td { border-bottom: none; }
  .report-meta td:first-child { width: 172px; }

  .period-title { position: absolute; left: 78px; top: 158px; font-size: 21px; font-weight: 700; }
  .market-status { position: absolute; right: 84px; top: 164px; font-size: 12.5px; font-weight: 700; }

  .signal-history { position: absolute; left: 78px; top: 214px; width: 690px; height: 150px; }
  .signal-month { position: absolute; width: 116px; text-align: center; top: 0; }
  .signal-month .signal { display: block; margin: 8px auto 0; }
  .signal-month .month-label { font-size: 12px; font-weight: 700; margin-top: 22px; }
  .signal-month.current { outline: 3px solid var(--frame-red); height: 116px; }
  .signal-month.current .month-label { position: absolute; left: 0; right: 0; top: 132px; margin: 0; }

  .index-chart { position: absolute; left: 78px; top: 374px; border: 1px solid #8a8a8a; }

  .signal-guide { position: absolute; left: 78px; top: 674px; width: 688px; border: 1px solid var(--rule); border-collapse: collapse; }
  .signal-guide td { border: 1px solid var(--rule); height: 69px; vertical-align: top; }
  .signal-guide .guide-icons { width: 164px; vertical-align: middle; }
  .guide-icons .icon-row { display: flex; align-items: center; justify-content: flex-end; padding-right: 28px; gap: 10px; }
  .guide-text { padding: 12px 0 0 18px; font-size: 12px; font-weight: 700; line-height: 1.25; }
  .guide-text .statement { display: block; max-width: 470px; }
  .guide-text .option { display: block; margin-top: 14px; }
  .guide-text .option.tight { margin-top: 2px; }

  .footer-rule { position: absolute; left: 78px; top: 1052px; width: 688px; height: 2px; background: var(--ink); }
  .advice { position: absolute; left: 78px; top: 1060px; width: 688px; font-size: 6.4px; font-weight: 700; line-height: 1.45; }
</style>
</head>
<body>

<svg width="0" height="0" style="position:absolute">
  <defs>
    <linearGradient id="housing-fill" x1="0" y1="0" x2="1" y2="0">
      <stop offset="0" stop-color="#3a3d44"/>
      <stop offset="0.5" stop-color="#1c1e23"/>
      <stop offset="1" stop-color="#0c0d10"/>
    </linearGradient>
    <linearGradient id="housing-rim" x1="0" y1="0" x2="0" y2="1">
      <stop offset="0" stop-color="#c9ccd2"/>
      <stop offset="1" stop-color="#5b5f66"/>
    </linearGradient>
    <radialGradient id="lens-shine" cx="38%" cy="32%" r="65%">
      <stop offset="0" stop-color="#ffffff" stop-opacity="0.7"/>
      <stop offset="0.35" stop-color="#ffffff" stop-opacity="0.12"/>
      <stop offset="1" stop-color="#000000" stop-opacity="0.25"/>
    </radialGradient>
    <filter id="halo" x="-80%" y="-80%" width="260%" height="260%">
      <feGaussianBlur stdDeviation="3.2"/>
    </filter>
    <symbol id="signal" viewBox="0 0 38 102" overflow="visible">
      <rect x="1" y="1" width="36" height="100" rx="11" fill="url(#housing-rim)"/>
      <rect x="3" y="3" width="32" height="96" rx="9.5" fill="url(#housing-fill)"/>
      <circle cx="19" cy="21" r="11.5" fill="#050506"/>
      <circle cx="19" cy="51" r="11.5" fill="#050506"/>
      <circle cx="19" cy="81" r="11.5" fill="#050506"/>
      <circle cx="19" cy="21" r="12" filter="url(#halo)" style="fill:var(--r);opacity:var(--rh)"/>
      <circle cx="19" cy="51" r="12" filter="url(#halo)" style="fill:var(--o);opacity:var(--oh)"/>
      <circle cx="19" cy="81" r="12" filter="url(#halo)" style="fill:var(--g);opacity:var(--gh)"/>
      <circle cx="19" cy="21" r="9.5" style="fill:var(--r)"/>
      <circle cx="19" cy="51" r="9.5" style="fill:var(--o)"/>
      <circle cx="19" cy="81" r="9.5" style="fill:var(--g)"/>
      <circle cx="19" cy="21" r="9.5" fill="url(#lens-shine)"/>
      <circle cx="19" cy="51" r="9.5" fill="url(#lens-shine)"/>
      <circle cx="19" cy="81" r="9.5" fill="url(#lens-shine)"/>
    </symbol>
    <symbol id="guide-arrow" viewBox="0 0 20 10">
      <path d="M0 3h12V0l8 5-8 5V7H0z" fill="var(--arrow)"/>
    </symbol>
  </defs>
</svg>

<div class="brand">
  <span class="brand-mark"></span>
  <span class="brand-name">earlynest</span>
</div>

<table class="report-meta">
  <tr><td>Country:</td><td>Australia</td></tr>
  <tr><td>Share Market Index:</td><td>Southern Composite 200 Index</td></tr>
  <tr><td>Investor:</td><td>Superannuation Saver</td></tr>
</table>

<h1 class="period-title">July 2014</h1>
<p class="market-status">Market conditions are favourable for equities.</p>

<div class="signal-history">
  <div class="signal-month" style="left:0"><svg class="signal signal-green" width="38" height="102"><use href="#signal"/></svg><p class="month-label">February 2014</p></div>
  <div class="signal-month" style="left:116px"><svg class="signal signal-green" width="38" height="102"><use href="#signal"/></svg><p class="month-label">March 2014</p></div>
  <div class="signal-month" style="left:232px"><svg class="signal signal-green" width="38" height="102"><use href="#signal"/></svg><p class="month-label">April 2014</p></div>
  <div class="signal-month" style="left:349px"><svg class="signal signal-green" width="38" height="102"><use href="#signal"/></svg><p class="month-label">May 2014</p></div>
  <div class="signal-month" style="left:464px"><svg class="signal signal-green" width="38" height="102"><use href="#signal"/></svg><p class="month-label">June 2014</p></div>
  <div class="signal-month current" style="left:574px"><svg class="signal signal-green" width="38" height="102"><use href="#signal"/></svg><p class="month-label">July 2014</p></div>
</div>

<svg class="index-chart" width="688" height="284" viewBox="65 312 573 236" font-family="Carlito, Calibri, sans-serif">
  <g class="signal-bands">
    <rect x="95" y="322" width="18" height="188" fill="var(--band-orange)"/>
    <rect x="113" y="322" width="5" height="188" fill="var(--band-red)"/>
    <rect x="118" y="322" width="5" height="188" fill="var(--band-orange)"/>
    <rect x="123" y="322" width="42" height="188" fill="var(--band-red)"/>
    <rect x="165" y="322" width="4" height="188" fill="var(--band-orange)"/>
    <rect x="169" y="322" width="5" height="188" fill="var(--band-red)"/>
    <rect x="174" y="322" width="6" height="188" fill="var(--band-orange)"/>
    <rect x="180" y="322" width="32" height="188" fill="var(--band-red)"/>
    <rect x="212" y="322" width="4" height="188" fill="var(--band-orange)"/>
    <rect x="216" y="322" width="19" height="188" fill="var(--band-red)"/>
    <rect x="235" y="322" width="25" height="188" fill="var(--band-orange)"/>
    <rect x="260" y="322" width="4" height="188" fill="var(--band-red)"/>
    <rect x="264" y="322" width="9" height="188" fill="var(--band-orange)"/>
    <rect x="273" y="322" width="3" height="188" fill="var(--band-green)"/>
    <rect x="276" y="322" width="20" height="188" fill="var(--band-orange)"/>
    <rect x="296" y="322" width="9" height="188" fill="var(--band-green)"/>
    <rect x="305" y="322" width="5" height="188" fill="var(--band-orange)"/>
    <rect x="310" y="322" width="8" height="188" fill="var(--band-green)"/>
    <rect x="318" y="322" width="7" height="188" fill="var(--band-orange)"/>
    <rect x="325" y="322" width="48" height="188" fill="var(--band-green)"/>
    <rect x="373" y="322" width="10" height="188" fill="var(--band-orange)"/>
    <rect x="383" y="322" width="47" height="188" fill="var(--band-red)"/>
    <rect x="430" y="322" width="10" height="188" fill="var(--band-orange)"/>
    <rect x="440" y="322" width="5" height="188" fill="var(--band-green)"/>
    <rect x="445" y="322" width="43" height="188" fill="var(--band-orange)"/>
    <rect x="488" y="322" width="3" height="188" fill="var(--band-green)"/>
    <rect x="491" y="322" width="14" height="188" fill="var(--band-orange)"/>
    <rect x="505" y="322" width="3" height="188" fill="var(--band-green)"/>
    <rect x="508" y="322" width="7" height="188" fill="var(--band-orange)"/>
    <rect x="515" y="322" width="4" height="188" fill="var(--band-red)"/>
    <rect x="519" y="322" width="21" height="188" fill="var(--band-orange)"/>
    <rect x="540" y="322" width="68" height="188" fill="var(--band-green)"/>
  </g>
  <polyline class="index-line" fill="none" stroke="#111" stroke-width="1.6" stroke-linejoin="round"
    points="95,463 110,461.1 120,455.5 135,457.4 150,451.7 158,463 170,451.7 185,455.5 195,463 210,469.6 220,460.2 240,453.6 260,446.1 275,430.1 285,434.8 300,420.7 315,406.6 320,397.2 330,406.6 345,387.8 360,369 372,350.2 378,364.3 385,387.8 395,392.5 405,444.2 415,455.5 425,439.5 440,416 450,408.5 455,417.9 465,411.3 470,425.4 480,411.3 495,408.5 510,434.8 520,430.1 530,436.7 540,425.4 555,416 565,397.2 575,401.9 585,389.7 595,392.5 605,389.7 608,392.5"/>
  <g class="y-axis" font-size="7.5" fill="#111">
    <text x="613" y="325">250</text><text x="613" y="344">230</text><text x="613" y="363">210</text>
    <text x="613" y="382">190</text><text x="613" y="400">170</text><text x="613" y="419">150</text>
    <text x="613" y="438">130</text><text x="613" y="457">110</text><text x="613" y="476">90</text>
    <text x="613" y="494">70</text><text x="613" y="513">50</text>
  </g>
  <g class="x-axis" font-size="8" fill="#111" text-anchor="end">
    <text transform="translate(98,516) rotate(-45)">Dec - 99</text>
    <text transform="translate(116,516) rotate(-45)">Jun - 00</text>
    <text transform="translate(133,516) rotate(-45)">Dec - 00</text>
    <text transform="translate(151,516) rotate(-45)">Jun - 01</text>
    <text transform="translate(169,516) rotate(-45)">Dec - 01</text>
    <text transform="translate(186,516) rotate(-45)">Jun - 02</text>
    <text transform="translate(204,516) rotate(-45)">Dec - 02</text>
    <text transform="translate(222,516) rotate(-45)">Jun - 03</text>
    <text transform="translate(240,516) rotate(-45)">Dec - 03</text>
    <text transform="translate(257,516) rotate(-45)">Jun - 04</text>
    <text transform="translate(275,516) rotate(-45)">Dec - 04</text>
    <text transform="translate(293,516) rotate(-45)">Jun - 05</text>
    <text transform="translate(310,516) rotate(-45)">Dec - 05</text>
    <text transform="translate(328,516) rotate(-45)">Jun - 06</text>
    <text transform="translate(346,516) rotate(-45)">Dec - 06</text>
    <text transform="translate(363,516) rotate(-45)">Jun - 07</text>
    <text transform="translate(381,516) rotate(-45)">Dec - 07</text>
    <text transform="translate(399,516) rotate(-45)">Jun - 08</text>
    <text transform="translate(417,516) rotate(-45)">Dec - 08</text>
    <text transform="translate(434,516) rotate(-45)">Jun - 09</text>
    <text transform="translate(452,516) rotate(-45)">Dec - 09</text>
    <text transform="translate(470,516) rotate(-45)">Jun - 10</text>
    <text transform="translate(487,516) rotate(-45)">Dec - 10</text>
    <text transform="translate(505,516) rotate(-45)">Jun - 11</text>
    <text transform="translate(523,516) rotate(-45)">Dec - 11</text>
    <text transform="translate(540,516) rotate(-45)">Jun - 12</text>
    <text transform="translate(558,516) rotate(-45)">Dec - 12</text>
    <text transform="translate(576,516) rotate(-45)">Jun - 13</text>
    <text transform="translate(593,516) rotate(-45)">Dec - 13</text>
    <text transform="translate(611,516) rotate(-45)">Jun - 14</text>
  </g>
</svg>

<table class="signal-guide">
  <tr>
    <td class="guide-icons"><div class="icon-row">
      <svg class="signal signal-green" width="23" height="62"><use href="#signal"/></svg>
    </div></td>
    <td class="guide-text"><span class="statement">If the signal is Green, it is recommended to be 100% invested in the aggressive strategy.</span><span class="option">Growth Superannuation Option</span></td>
  </tr>
  <tr>
    <td class="guide-icons"><div class="icon-row">
      <svg class="signal signal-green" width="23" height="62"><use href="#signal"/></svg>
      <svg width="20" height="10"><use href="#guide-arrow"/></svg>
      <svg class="signal signal-orange" width="23" height="62"><use href="#signal"/></svg>
    </div></td>
    <td class="guide-text"><span class="statement">If the signal changes from Green to Orange, it is recommended to reduce your risk exposure.</span><span class="option">Balanced Superannuation Option</span></td>
  </tr>
  <tr>
    <td class="guide-icons"><div class="icon-row">
      <svg class="signal signal-orange" width="23" height="62"><use href="#signal"/></svg>
      <svg width="20" height="10"><use href="#guide-arrow"/></svg>
      <svg class="signal signal-red" width="23" height="62"><use href="#signal"/></svg>
    </div></td>
    <td class="guide-text"><span class="statement">If the signal changes from Orange to Red, it is recommended to reduce your risk as much as possible.</span><span class="option tight">Cash Superannuation Option</span></td>
  </tr>
  <tr>
    <td class="guide-icons"><div class="icon-row">
      <svg class="signal signal-red" width="23" height="62"><use href="#signal"/></svg>
      <svg width="20" height="10"><use href="#guide-arrow"/></svg>
      <svg class="signal signal-orange" width="23" height="62"><use href="#signal"/></svg>
    </div></td>
    <td class="guide-text"><span class="statement">If the signal changes from Red to Orange, it is recommended to increase your risk exposure .</span><span class="option">Balanced Superannuation Option</span></td>
  </tr>
  <tr>
    <td class="guide-icons"><div class="icon-row">
      <svg class="signal signal-orange" width="23" height="62"><use href="#signal"/></svg>
      <svg width="20" height="10"><use href="#guide-arrow"/></svg>
      <svg class="signal signal-green" width="23" height="62"><use href="#signal"/></svg>
    </div></td>
    <td class="guide-text"><span class="statement">If the signal changes from Orange to Green, it is recommended to increase your risk exposure .</span><span class="option">Growth Superannuation Option</span></td>
  </tr>
</table>

<div class="footer-rule"></div>
<p class="advice">Advice Warning: This website is intended to provide general financial information only and has been prepared by Summit Analytics without taking into account any particular person's objectives,<br>financial situation or needs. Investors should, before acting on this information, consider the appropriateness of this information having regard to their personal objectives, financial situation or needs.<br>We recommend investors obtain financial advice specific to their situation before making any financial investment decision.</p>

</body>
</html>
```